Business Card Design

We would like a colorful, engaging, welcoming business card, utilizing our picture of a local lighthouse. We are a Church. We would like the design to mostly feature the colour blue.
Updates
Project Deadline Extended
Reason: Because of some suggested changes that have been sent out
Thank you so much to all Designers who sent in submissions to us - it was really hard to make a decision, they were all of such high quality. We would not hesitate to recommend Sketch Harbor to other churches/ businesses.
Kestrel Beacon Fellowship
Industry/Entity Type
Business
Contact Information for Business Card
Kestrel Beacon Fellowship Inc, 17 Marrick Rd, TOVERDALE WA 6391, Ph: (08) 9517 4063, E: beaconfellowship@quorvamail.example, Facebook logo - Kestrel Beacon Fellowship Inc, Sunday Service 10am, "For God sent not his Son into the world to condemn the world; but that the world through Him might be saved." John 3:17.
Look and feel
Each slider illustrates characteristics of the customer's brand and the style your logo design should communicate.

```html
<!DOCTYPE html>
<html lang="en">
<head>
<meta charset="utf-8">
<title>Kestrel Beacon Fellowship – Business Card</title>
<link href="https://fonts.googleapis.com/css2?family=Lato:ital,wght@0,400;0,700;1,400&display=swap" rel="stylesheet">
<style>
  :root {
    --page-bg: #d9dadc;
    --card-black: #000000;
    --accent-blue: #9ab8e8;
    --crescent-blue: #8fb0e0;
    --quote-ink: #d6e2f5;
    --band-ink: #0b0f18;
    --badge-tan: #e6c98c;
  }
  * { margin: 0; padding: 0; box-sizing: border-box; }
  html, body {
    width: 1200px;
    height: 926px;
    overflow: hidden;
    background: var(--page-bg);
    font-family: "Lato", sans-serif;
  }
  .card {
    position: absolute;
    left: 100px;
    top: 178px;
    width: 1000px;
    height: 570px;
    background: var(--card-black);
    overflow: hidden;
    box-shadow: 0 6px 18px rgba(0,0,0,0.25);
  }
  .card-art {
    position: absolute;
    inset: 0;
    width: 1000px;
    height: 570px;
  }
  .verse {
    position: absolute;
    left: 34px;
    top: 268px;
    width: 400px;
    font-style: italic;
    font-size: 27px;
    line-height: 1.2;
    color: var(--quote-ink);
  }
  .verse-ref {
    display: block;
    text-align: right;
    padding-right: 40px;
    margin-top: 6px;
  }
  .org-name {
    position: absolute;
    right: 44px;
    top: 44px;
    text-align: right;
    font-weight: 700;
    font-size: 46px;
    line-height: 1.05;
    color: var(--accent-blue);
    text-transform: uppercase;
  }
  .org-name .suffix { text-transform: none; }
  .contact {
    position: absolute;
    right: 40px;
    top: 312px;
    text-align: right;
    color: var(--accent-blue);
    font-size: 20px;
    line-height: 1.35;
    white-space: nowrap;
  }
  .contact .phone { font-size: 30px; line-height: 1.25; }
  .contact .email { font-size: 19px; }
  .service-band {
    position: absolute;
    left: 450px;
    right: 0;
    top: 448px;
    height: 58px;
    background: linear-gradient(90deg, #000000 0%, #3a4860 35%, var(--accent-blue) 75%);
    display: flex;
    align-items: center;
    justify-content: flex-end;
    padding-right: 70px;
    font-weight: 700;
    font-size: 30px;
    letter-spacing: 0.5px;
    color: var(--band-ink);
  }
</style>
</head>
<body>
  <div class="card">
    <svg class="card-art" viewBox="0 0 1000 570" xmlns="http://www.w3.org/2000/svg">
      <defs>
        <linearGradient id="photoTone" x1="0" y1="0" x2="0" y2="1">
          <stop offset="0" stop-color="#2c5fd8"/>
          <stop offset="0.3" stop-color="#1a3fae"/>
          <stop offset="0.45" stop-color="#0c2474"/>
          <stop offset="0.55" stop-color="#1b231c"/>
          <stop offset="1" stop-color="#0a0d0a"/>
        </linearGradient>
      </defs>
      <path role="img" aria-label="Photograph of a local lighthouse beaming light over a dark hill at night"
            d="M0,0 L520,0 Q650,250 430,570 L0,570 Z" fill="url(#photoTone)"/>
      <path class="crescent" d="M520,0 L575,0 Q680,260 450,570 L430,570 Q650,250 520,0 Z" fill="var(--crescent-blue)"/>
      <circle class="social-badge" cx="470" cy="477" r="15" fill="var(--badge-tan)"/>
    </svg>

    <p class="verse">“For God sent not his Son into the world to condemn the world; but that the world through Him might be saved.”<span class="verse-ref">-John 3:17</span></p>

    <h1 class="org-name">Kestrel<br>Beacon<br>Fellowship<br><span class="suffix">Inc.</span></h1>

    <div class="contact">
      <div class="phone">(08) 9517 4063</div>
      <div class="email">beaconfellowship@quorvamail.example</div>
      <div class="address">17 Marrick Rd, TOVERDALE WA 6391</div>
    </div>

    <div class="service-band">SUNDAY SERVICE 10AM</div>
  </div>
</body>
</html>
```